Business card design needed

We are a start up Mobile Vet Clinic.
We will be servicing an are that cover the Gladstone Region Shire.
Bookings will be made via the number listed or email address.
Travel will be charged

Target Market(s)

Pet Owners

Industry/Entity Type

Business

Contact Information for Business Card

BRINDELLA MOBILE VET
Tarrowen Pty Ltd
Dana Fosterby BVSc
27 Wexhaven St
Merrowdale QLD 4712

PH: 0743186209 Fax: 0743186514 email: bmvet@quillnet.example

Logo styles of interest
Pictorial/Combination Logo

```html
<!DOCTYPE html>
<html lang="en">
<head>
<meta charset="utf-8">
<title>Brindella Mobile Vet – Business Card</title>
<link rel="stylesheet" href="https://fonts.googleapis.com/css2?family=Fredoka:wght@500;600;700&display=swap">
<style>
  :root {
    --card-bg: #131517;
    --band-top: #3e0909;
    --band-bottom: #730000;
    --title-ink: #121212;
    --badge-fill: #55595e;
    --badge-edge: #d8dadc;
    --note-ink: #a4a9a9;
    --bullet: #474c52;
    --rule: #2c2f32;
    --footer-ink: #ffffff;
  }
  * { margin: 0; padding: 0; box-sizing: border-box; }
  html, body {
    width: 1200px;
    height: 695px;
    overflow: hidden;
    background: var(--card-bg);
  }
  .card {
    position: relative;
    width: 1200px;
    height: 695px;
    background: var(--card-bg);
    font-family: "Fredoka", "Trebuchet MS", sans-serif;
    overflow: hidden;
  }
  .band {
    position: absolute;
    top: 48px;
    height: 162px;
    background: linear-gradient(to bottom, var(--band-top), var(--band-bottom));
    box-shadow: 0 4px 10px rgba(0, 0, 0, 0.6);
  }
  .band--left { left: 0; width: 46px; }
  .band--title {
    left: 391px;
    right: 0;
    display: flex;
    align-items: center;
    justify-content: center;
  }
  .brand-title {
    color: var(--title-ink);
    font-weight: 700;
    font-size: 58px;
    letter-spacing: 2px;
    line-height: 1;
    margin-top: -6px;
    white-space: nowrap;
  }
  .brand-mark {
    position: absolute;
    left: 100px;
    top: 66px;
    width: 236px;
    display: flex;
    flex-direction: column;
    align-items: center;
    gap: 16px;
  }
  .brand-mark__disc {
    width: 150px;
    height: 150px;
    border-radius: 50%;
    background: var(--badge-fill);
    border: 4px solid var(--badge-edge);
  }
  .brand-mark__name {
    color: var(--badge-edge);
    font-weight: 600;
    font-size: 24px;
    letter-spacing: 2px;
  }
  .notes {
    position: absolute;
    left: 164px;
    top: 466px;
    list-style: none;
  }
  .notes li {
    display: flex;
    align-items: center;
    gap: 11px;
    color: var(--note-ink);
    font-weight: 700;
    font-size: 17.5px;
    letter-spacing: 0.7px;
    height: 28px;
    white-space: nowrap;
  }
  .notes li::before {
    content: "";
    width: 13px;
    height: 13px;
    border-radius: 50%;
    background: var(--bullet);
    flex: none;
  }
  .rule {
    position: absolute;
    left: 31px;
    right: 34px;
    top: 573px;
    height: 2px;
    background: var(--rule);
  }
  .contact {
    position: absolute;
    left: 157px;
    width: 880px;
    color: var(--footer-ink);
    font-weight: 600;
    font-size: 22.5px;
    letter-spacing: 1.1px;
    line-height: 1;
    white-space: nowrap;
  }
  .contact--company { top: 590px; }
  .contact--lines {
    top: 634px;
    display: flex;
    justify-content: space-between;
  }
</style>
</head>
<body>
  <main class="card">
    <div class="band band--left"></div>
    <div class="band band--title">
      <h1 class="brand-title">BRINDELLA MOBILE VET</h1>
    </div>

    <div class="brand-mark">
      <div class="brand-mark__disc"></div>
      <span class="brand-mark__name">BRINDELLA</span>
    </div>

    <ul class="notes">
      <li>Bookings will be made via the number listed or email address.</li>
      <li>Travel will be charged.</li>
    </ul>

    <div class="rule"></div>

    <p class="contact contact--company">Tarrowen Pty Ltd Dana Fosterby BVSc 27 Wexhaven St Merrowdale QLD 4712</p>
    <p class="contact contact--lines">
      <span class="phone">PH: 0743186209 Fax: 0743186514</span>
      <span class="email">email: bmvet@quillnet.example</span>
    </p>
  </main>
</body>
</html>
```